Brochure design for trade company

I would like to get a professional, easy to read and eye catchy capability statement designed for my electrical business.

My aim is to be able to go to property managers and WOW them when they see the capability statement.

Attached the content writing, design brief, company logo and template of what I like below. If there are any questions please send me a message.

The areas we service photo is an example, please do your own designs for the maps section

Thank you in advance for the help team.

Requirements
Must have
• The areas we service photo is an example, please do your own designs for the maps section
Nice to have
• Eye catching and creative. Also be warm & inviting
Should not have
• Not too out of place looking photos or elements. Don’t make it he design look too cold

```html
<!DOCTYPE html>
<html lang="en">
<head>
<meta charset="utf-8">
<title>Voltline Electrical – Capability Statement</title>
<link rel="stylesheet" href="https://fonts.googleapis.com/css2?family=Barlow+Condensed:wght@400;500;600;700&family=Roboto:wght@300;400;500;700&display=swap">
<style>
:root{
  --bg:#a6a6a6;
  --black:#000000;
  --orange:#f7981d;
  --white:#ffffff;
  --mist:#dfe1e5;
  --ink:#1a1a1a;
  --body:#333333;
  --head:"Barlow Condensed",sans-serif;
  --text:"Roboto",sans-serif;
}
*{margin:0;padding:0;box-sizing:border-box}
html,body{width:1200px;height:3504px;overflow:hidden;background:var(--bg);font-family:var(--text)}
.page{position:absolute;left:250px;width:700px;overflow:hidden;box-shadow:10px 12px 14px rgba(0,0,0,.35)}
.abs{position:absolute}
.brand{font-family:var(--head);font-weight:700;color:var(--white);letter-spacing:2px;text-transform:uppercase;text-align:center;line-height:1}

/* cover */
.cover{top:200px;height:981px;background:var(--black)}
.cover .brand{top:72px;left:0;width:700px;font-size:36px}
.cover-title{top:188px;left:0;width:700px;text-align:center;font-family:var(--head);font-weight:600;font-size:56px;color:var(--white);letter-spacing:.5px}
.cover-title span{color:var(--orange)}
.cover-sub{top:256px;left:0;width:700px;text-align:center;font-family:var(--head);font-weight:400;font-size:28px;color:var(--white)}
.city-photo{top:373px;left:0;width:700px;height:430px;background:linear-gradient(180deg,#3a4a7a 0%,#4f5d8c 30%,#c08a3a 62%,#3a3550 78%,#1f2f5a 100%)}
.sector-band{top:803px;left:0;width:700px;height:56px;background:var(--orange);display:flex;align-items:center;justify-content:center;font-family:var(--text);font-weight:500;font-size:17px;letter-spacing:4.6px;color:var(--black)}
.cover-url{top:897px;left:0;width:700px;text-align:center;font-weight:500;font-size:20px;letter-spacing:4.5px;color:var(--orange)}

/* about */
.about{top:1238px;height:981px;background:var(--black)}
.about-top{top:0;left:0;width:700px;height:572px;background:var(--mist)}
.tag{top:59px;left:57px;height:43px;padding:0 10px;background:var(--orange);color:var(--white);font-family:var(--head);font-weight:600;font-size:34px;letter-spacing:6px;line-height:43px}
.about-title{top:106px;left:57px;font-family:var(--head);font-weight:700;font-size:58px;line-height:57px;color:var(--black)}
.who{top:272px;left:57px;font-family:var(--head);font-weight:600;font-size:32px;color:var(--ink)}
.who-copy{top:328px;left:57px;width:272px;font-size:12.6px;line-height:16.5px;color:var(--body)}
.who-copy p{margin-bottom:16px}
.who-copy p.tight{margin-bottom:0}
.worker-photo{top:27px;left:349px;width:351px;height:545px;background:linear-gradient(160deg,#e8e9ec 0%,#d8dadf 40%,#c9ccd3 100%)}
.values{top:572px;left:0;width:700px;height:149px;background:var(--orange)}
.values h3{position:absolute;top:22px;left:0;width:700px;text-align:center;font-family:var(--text);font-weight:700;font-size:27px;letter-spacing:13px;color:var(--black)}
.value-row{position:absolute;top:78px;left:55px;display:flex;gap:0}
.value{display:flex;align-items:center;gap:8px;font-size:12.6px;line-height:16px;color:var(--black)}
.value svg{width:44px;height:44px;flex:none}
.promise-photo{top:721px;left:0;width:213px;height:260px;background:linear-gradient(150deg,#c9b7a6 0%,#e6d9cc 45%,#8aa2bd 100%)}
.promise{top:746px;left:226px}
.promise h3{font-family:var(--head);font-weight:600;font-size:35px;color:var(--orange)}
.ticks{list-style:none;margin-top:14px;width:410px}
.ticks li{position:relative;padding-left:20px;font-size:12.6px;line-height:16.5px;margin-bottom:5px}
.ticks li svg{position:absolute;left:0;top:2px;width:12px;height:12px}
.promise .ticks li{color:var(--white)}

/* services */
.services{top:2278px;height:980px;background:var(--white)}
.sec-head{font-family:var(--head);font-weight:600;font-size:36px;line-height:37px;color:var(--orange)}
.areas{top:52px;left:52px}
.map{top:145px;left:52px;width:272px;height:297px;background:linear-gradient(135deg,#f2f3f2 0%,#e9ebea 60%,#cfded8 100%)}
.map-frame{top:177px;left:82px;width:210px;height:202px;border:2.5px dashed var(--orange)}
.maint{top:52px;left:374px}
.services .ticks{top:150px;left:374px;width:290px}
.services .ticks li{color:var(--body);font-size:12.4px;margin-bottom:5.4px}
.reviews{top:491px;left:0;width:700px;height:202px;background:var(--orange)}
.review{position:absolute;top:44px;width:250px}
.review .q{position:absolute;left:-50px;top:-2px;font-family:var(--head);font-weight:700;font-size:54px;line-height:40px;color:var(--black)}
.review p{font-family:var(--head);font-weight:500;font-size:13.2px;line-height:13.4px;color:var(--black)}
.review .who-name{display:flex;align-items:center;gap:10px;margin-top:10px;font-family:var(--head);font-weight:500;font-size:20px;color:var(--black)}
.stars{border:1.5px solid var(--black);padding:0 4px;font-size:15px;letter-spacing:1px;line-height:21px}
.footer{top:693px;left:0;width:700px;height:287px;background:var(--black)}
.footer .brand{top:137px;left:95px;width:180px;font-size:26px}
.contact{top:48px;left:370px;color:var(--white)}
.contact .name{font-family:var(--head);font-size:26px;color:var(--white)}
.contact .name b{font-weight:600;color:var(--orange)}
.contact .line{font-family:var(--head);font-weight:500;font-size:15px;line-height:17px}
.contact .lbl{color:var(--orange);font-weight:600}
.contact .url{font-family:var(--head);font-weight:600;font-size:23px;color:var(--orange);margin-top:28px}
</style>
</head>
<body>

<section class="page cover">
  <div class="abs brand">Voltline Electrical</div>
  <h1 class="abs cover-title">CAPABILITY <span>STATEMENT</span></h1>
  <p class="abs cover-sub">When quality and reliability counts</p>
  <div class="abs city-photo" role="img" aria-label="Night city harbour skyline with lit towers reflected in the water"></div>
  <div class="abs sector-band">Residential | Commercial | Real Estate | Strata</div>
  <div class="abs cover-url">voltlineelectrical.com.au</div>
</section>

<section class="page about">
  <div class="abs about-top"></div>
  <div class="abs worker-photo" role="img" aria-label="Smiling electrician in hard hat and overalls giving a thumbs up while carrying a cable coil"></div>
  <div class="abs tag">ABOUT</div>
  <h2 class="abs about-title">VOLTLINE<br>ELECTRICAL</h2>
  <h3 class="abs who">Who we are</h3>
  <div class="abs who-copy">
    <p>Voltline Electrical, we’re more than just a team of electricians—we’re your extended family that you can rely on 24/7 for reliable, expert help for anything electrical related.</p>
    <p class="tight">With our friendly, reliable, and no-nonsense approach, we ensure that your needs are met with professionalism and a smile.</p>
    <p>Whether it’s a small repair or a major installation, we’re here to make your life easier.</p>
    <p>At Voltline Electrical, we make sure that every job counts.</p>
  </div>
  <div class="abs values">
    <h3>CORE VALUES</h3>
    <div class="value-row">
      <div class="value" style="width:153px">
        <svg viewBox="0 0 44 44" fill="none" stroke="#000" stroke-width="1.8"><circle cx="22" cy="24" r="9"/><path d="M18 24l3 3 5-6"/><path d="M16 32l-3 9 5-2 3 4 1-8M28 32l3 9-5-2-3 4"/><path d="M8 10l2 2M22 4v3M36 10l-2 2M6 20h3M38 20h-3"/></svg>
        <span>Reliability and<br>safety first</span>
      </div>
      <div class="value" style="width:158px">
        <svg viewBox="0 0 44 44" fill="none" stroke="#000" stroke-width="1.8"><circle cx="22" cy="10" r="4"/><circle cx="11" cy="15" r="3.5"/><circle cx="33" cy="15" r="3.5"/><path d="M15 26c0-5 3-9 7-9s7 4 7 9M5 27c0-4 2-7 6-7M39 27c0-4-2-7-6-7"/><path d="M4 30c6 0 10 10 18 10s12-10 18-10"/></svg>
        <span>Community and<br>respect</span>
      </div>
      <div class="value" style="width:134px">
        <svg viewBox="0 0 44 44" fill="none" stroke="#000" stroke-width="1.8"><path d="M8 24a14 14 0 0 1 28 0"/><rect x="4" y="22" width="6" height="11" rx="2"/><rect x="34" y="22" width="6" height="11" rx="2"/><circle cx="22" cy="26" r="8"/><circle cx="19" cy="26" r="1" fill="#000"/><circle cx="22" cy="26" r="1" fill="#000"/><circle cx="25" cy="26" r="1" fill="#000"/></svg>
        <span>Customer<br>Focused</span>
      </div>
      <div class="value" style="width:160px">
        <svg viewBox="0 0 44 44" fill="none" stroke="#000" stroke-width="1.8"><path d="M22 39L7 24a8 8 0 0 1 15-11 8 8 0 0 1 15 11z"/><path d="M14 24l6 6 4-4 6 6M20 20l4 4"/></svg>
        <span>Openness, trust<br>and accountability</span>
      </div>
    </div>
  </div>
  <div class="abs promise-photo" role="img" aria-label="Happy family of four embracing and smiling"></div>
  <div class="abs promise">
    <h3>Our promise to you</h3>
    <ul class="ticks">
      <li><svg viewBox="0 0 12 12"><circle cx="6" cy="6" r="6" fill="#f7981d"/><path d="M3.3 6.2l1.8 1.8 3.6-3.6" stroke="#000" stroke-width="1.4" fill="none"/></svg>Around clock communication. We can always be reached 24/7</li>
      <li><svg viewBox="0 0 12 12"><circle cx="6" cy="6" r="6" fill="#f7981d"/><path d="M3.3 6.2l1.8 1.8 3.6-3.6" stroke="#000" stroke-width="1.4" fill="none"/></svg>Service with a smile on our &nbsp;face. We take the stress out of daily life and let you do the things you want to do</li>
      <li><svg viewBox="0 0 12 12"><circle cx="6" cy="6" r="6" fill="#f7981d"/><path d="M3.3 6.2l1.8 1.8 3.6-3.6" stroke="#000" stroke-width="1.4" fill="none"/></svg>Reliability and speed, quotations and WO’s actioned promptly</li>
      <li><svg viewBox="0 0 12 12"><circle cx="6" cy="6" r="6" fill="#f7981d"/><path d="M3.3 6.2l1.8 1.8 3.6-3.6" stroke="#000" stroke-width="1.4" fill="none"/></svg>All our staff are trained to the highest level with expert knowledge in the industry to make a tailored solution for clients</li>
    </ul>
  </div>
</section>

<section class="page services">
  <h2 class="abs sec-head areas">AREAS<br>WE SERVICE</h2>
  <div class="abs map" role="img" aria-label="Street map of the metropolitan service region with suburbs and coastline"></div>
  <div class="abs map-frame"></div>
  <h2 class="abs sec-head maint">Our maintenance<br>services</h2>
  <ul class="abs ticks">
    <li><svg viewBox="0 0 12 12"><circle cx="6" cy="6" r="6" fill="#f7981d"/><path d="M3.3 6.2l1.8 1.8 3.6-3.6" stroke="#fff" stroke-width="1.4" fill="none"/></svg>24/7 Emergency services</li>
    <li><svg viewBox="0 0 12 12"><circle cx="6" cy="6" r="6" fill="#f7981d"/><path d="M3.3 6.2l1.8 1.8 3.6-3.6" stroke="#fff" stroke-width="1.4" fill="none"/></svg>Fault finding and diagnostics</li>
    <li><svg viewBox="0 0 12 12"><circle cx="6" cy="6" r="6" fill="#f7981d"/><path d="M3.3 6.2l1.8 1.8 3.6-3.6" stroke="#fff" stroke-width="1.4" fill="none"/></svg>Switchboard upgrade and repairs</li>
    <li><svg viewBox="0 0 12 12"><circle cx="6" cy="6" r="6" fill="#f7981d"/><path d="M3.3 6.2l1.8 1.8 3.6-3.6" stroke="#fff" stroke-width="1.4" fill="none"/></svg>General lighting installations &amp; repairs</li>
    <li><svg viewBox="0 0 12 12"><circle cx="6" cy="6" r="6" fill="#f7981d"/><path d="M3.3 6.2l1.8 1.8 3.6-3.6" stroke="#fff" stroke-width="1.4" fill="none"/></svg>PowerPoint installation</li>
    <li><svg viewBox="0 0 12 12"><circle cx="6" cy="6" r="6" fill="#f7981d"/><path d="M3.3 6.2l1.8 1.8 3.6-3.6" stroke="#fff" stroke-width="1.4" fill="none"/></svg>Electric storage hot water systems service</li>
    <li><svg viewBox="0 0 12 12"><circle cx="6" cy="6" r="6" fill="#f7981d"/><path d="M3.3 6.2l1.8 1.8 3.6-3.6" stroke="#fff" stroke-width="1.4" fill="none"/></svg>Smoke alarm installation and compliance</li>
    <li><svg viewBox="0 0 12 12"><circle cx="6" cy="6" r="6" fill="#f7981d"/><path d="M3.3 6.2l1.8 1.8 3.6-3.6" stroke="#fff" stroke-width="1.4" fill="none"/></svg>Appliance repair/ installations</li>
    <li><svg viewBox="0 0 12 12"><circle cx="6" cy="6" r="6" fill="#f7981d"/><path d="M3.3 6.2l1.8 1.8 3.6-3.6" stroke="#fff" stroke-width="1.4" fill="none"/></svg>Ventiatlion &amp; mould prevention – ceiling fans, exhaust fans, underfloor ventilation</li>
    <li><svg viewBox="0 0 12 12"><circle cx="6" cy="6" r="6" fill="#f7981d"/><path d="M3.3 6.2l1.8 1.8 3.6-3.6" stroke="#fff" stroke-width="1.4" fill="none"/></svg>TV,Data and antenna services</li>
    <li><svg viewBox="0 0 12 12"><circle cx="6" cy="6" r="6" fill="#f7981d"/><path d="M3.3 6.2l1.8 1.8 3.6-3.6" stroke="#fff" stroke-width="1.4" fill="none"/></svg>Surge protection</li>
    <li><svg viewBox="0 0 12 12"><circle cx="6" cy="6" r="6" fill="#f7981d"/><path d="M3.3 6.2l1.8 1.8 3.6-3.6" stroke="#fff" stroke-width="1.4" fill="none"/></svg>EV charging systems and lighting upgrades for commercial premises</li>
  </ul>

  <div class="abs reviews">
    <div class="review" style="left:96px">
      <span class="q">“</span>
      <p>Lorem ipsum dolor sit amet, consectetur adipiscing elit. Integer vehicula justo nec lacus tempor, vitae pellentesque lorem dapibus. Mauris vitae lorem quis lorem volutpat scelerisque eget eu sem. Nam et congue sem. Etiam tristique sit amet mi ac feugiat.</p>
      <div class="who-name">John Doe <span class="stars">★★★★★</span></div>
    </div>
    <div class="review" style="left:414px">
      <span class="q">“</span>
      <p>Lorem ipsum dolor sit amet, consectetur adipiscing elit. Integer vehicula justo nec lacus tempor, vitae pellentesque lorem dapibus. Mauris vitae lorem quis lorem volutpat scelerisque eget eu sem. Nam et congue sem. Etiam tristique sit amet mi ac feugiat.</p>
      <div class="who-name">John Doe <span class="stars">★★★★★</span></div>
    </div>
  </div>

  <div class="abs footer">
    <div class="abs brand">Voltline Electrical</div>
    <div class="abs contact">
      <div class="name"><b>Daniel Reyes</b> – Director</div>
      <div class="line" style="margin-top:10px">0400 318 275<br>Services@voltlineelectrical.com.au</div>
      <div class="line" style="margin-top:16px"><span class="lbl">Electrical supervisors licence :</span> 412397C</div>
      <div class="line" style="margin-top:16px"><span class="lbl">Company ABN :</span> 48 203 915 776</div>
      <div class="url">voltlineelectrical.com.au</div>
    </div>
  </div>
</section>

</body>
</html>
```